Need a business card portraying store logo and up and coming business of quilt fabrics, apparel fabrics, notions and buttons. Our business name is Willow Bolt Quilts and Notions. Am attaching logo. The design should communicate a growing business and warm atmosphere. Would like address and store hours and contact info displayed on card. Mon - Fri 10:00 to 6:00, Saturday 10:00 to 2:00. Address 238 W Elm Ave, Newton, KS 67392 email: willowboltquilts@mailbarn.net. Phone and fax 316-555-2847. After hours contact # 620-555-3916 Also like vintage sewing machines and dress forms if it works to incorporate fine, if not thats ok too.

```html
<!DOCTYPE html>
<html lang="en">
<head>
<meta charset="utf-8">
<title>Willow Bolt Quilts and Notions — Business Card</title>
<link rel="stylesheet" href="https://fonts.googleapis.com/css2?family=Arimo:wght@400&display=swap">
<style>
  :root {
    --paper: #ffffff;
    --sky: #6dbde6;
    --lemon: #f7ff00;
    --crimson: #e0245e;
    --button-red: #dc2a1f;
    --ink-light: #ffffff;
  }
  html, body {
    margin: 0;
    padding: 0;
    overflow: hidden;
    background: var(--paper);
  }
  .card {
    position: relative;
    width: 1200px;
    height: 846px;
    overflow: hidden;
    background: var(--paper);
    font-family: "Arimo", Arial, sans-serif;
  }
  .brand {
    position: absolute;
    top: 112px;
    left: 0;
    width: 1200px;
    display: flex;
    align-items: center;
    justify-content: center;
    gap: 26px;
  }
  .brand-dot {
    width: 120px;
    height: 120px;
    border-radius: 50%;
    background: var(--button-red);
    flex: none;
  }
  .brand-name {
    margin: 0;
    font-size: 54px;
    font-weight: 400;
    color: var(--crimson);
    line-height: 1;
    white-space: nowrap;
  }
  .info-band {
    position: absolute;
    top: 432px;
    left: 0;
    width: 1200px;
    height: 265px;
    background: var(--sky);
  }
  .footer-band {
    position: absolute;
    top: 697px;
    left: 0;
    width: 1200px;
    height: 149px;
    background: var(--lemon);
  }
  .contact-icon {
    position: absolute;
    fill: var(--ink-light);
  }
  .contact-text {
    position: absolute;
    margin: 0;
    color: var(--ink-light);
    font-size: 16px;
    line-height: 19px;
    white-space: nowrap;
  }
  .contact-rule {
    position: absolute;
    height: 1px;
    background: var(--ink-light);
  }
  .band-title {
    position: absolute;
    left: 558px;
    width: 600px;
    margin: 0;
    text-align: center;
    font-weight: 400;
    line-height: 1;
    white-space: nowrap;
  }
  .band-title-main {
    top: 492px;
    font-size: 58px;
    color: var(--ink-light);
  }
  .band-title-sub {
    top: 565px;
    font-size: 54px;
    color: var(--lemon);
  }
</style>
</head>
<body>
<main class="card">
  <header class="brand">
    <span class="brand-dot" aria-hidden="true"></span>
    <h1 class="brand-name">Willow Bolt Quilts and Notions</h1>
  </header>

  <section class="info-band" aria-label="Store contact details"></section>

  <svg class="contact-icon" style="left:50px; top:444px" width="32" height="46" viewBox="0 0 32 46" aria-hidden="true">
    <path d="M16 0C7 0 0 7 0 16c0 11 16 30 16 30s16-19 16-30C32 7 25 0 16 0zm0 22a6 6 0 1 1 0-12 6 6 0 0 1 0 12z"/>
  </svg>
  <p class="contact-text" style="left:113px; top:450px">238 W Elm Ave<br>Kansas 67392</p>

  <svg class="contact-icon" style="left:47px; top:510px" width="46" height="32" viewBox="0 0 46 32" aria-hidden="true">
    <path d="M0 0h46v32H0z M3 3l20 17L43 3z" fill-rule="evenodd"/>
    <path d="M3 29l14-13M43 29L29 16" stroke="#6dbde6" stroke-width="2"/>
  </svg>
  <p class="contact-text" style="left:109px; top:520px">willowboltquilts@mailbarn.net</p>

  <svg class="contact-icon" style="left:48px; top:557px" width="40" height="48" viewBox="0 0 40 48" aria-hidden="true">
    <path d="M10 2c3-2 5-1 6 1l4 9c1 2 0 4-2 5l-3 2c1 5 5 12 10 15l3-2c2-1 4-1 5 1l5 8c1 2 1 4-1 5l-4 2C22 51 -6 20 6 5z"/>
  </svg>
  <p class="contact-text" style="left:113px; top:557px">316-555-2847</p>
  <span class="contact-rule" style="left:113px; top:581px; width:117px"></span>
  <p class="contact-text" style="left:115px; top:590px">620-555-3916</p>

  <svg class="contact-icon" style="left:53px; top:623px" width="38" height="42" viewBox="0 0 38 42" aria-hidden="true">
    <rect x="14" y="0" width="10" height="4"/>
    <rect x="17" y="3" width="4" height="4"/>
    <circle cx="19" cy="24" r="17" fill="none" stroke="#ffffff" stroke-width="4"/>
    <path d="M17 14h4v12h-4z"/>
  </svg>
  <p class="contact-text" style="left:116px; top:623px">Mon - Fri 10:00 to 6:00</p>
  <span class="contact-rule" style="left:113px; top:648px; width:185px"></span>
  <p class="contact-text" style="left:116px; top:653px">Saturday 10:00 to 2:00</p>

  <h2 class="band-title band-title-main">Willow Bolt Quilts</h2>
  <p class="band-title band-title-sub">and Notions</p>

  <footer class="footer-band" aria-hidden="true"></footer>
</main>
</body>
</html>
```